Business Card Design Project

Looking for a simple and stylish business card. We are an Advertising Company. The card Must feature the company logo (attached) and also this info.
p: 0481629054
e: sales@rv-promo.com.au
w: www.rv-promo.com.au
We Advertise mainly using TV screens featured in restaurants and cafe. See website for more about the business.
Not really looking for a plain background, but at the same time do not want to much happening in the Background. I am not really to fussy though with the design or the colour scheme, and I am leaving the creativity part up to you creative designers.

```html
<!DOCTYPE html>
<html lang="en">
<head>
<meta charset="utf-8">
<title>RVPROMO Business Card</title>
<link rel="stylesheet" href="https://fonts.googleapis.com/css2?family=Questrial&display=swap">
<style>
  :root {
    --paper: #ffffff;
    --ink: #111111;
    --brand-blue: #1238e0;
    --mark-grey: #2f3d52;
    --band-top: #e9ecf2;
    --band-bottom: #c9cfda;
  }
  html, body {
    margin: 0;
    padding: 0;
    overflow: hidden;
    background: var(--paper);
  }
  .card {
    position: relative;
    width: 741px;
    height: 1200px;
    background: var(--paper);
    overflow: hidden;
    font-family: "Questrial", "Century Gothic", sans-serif;
    color: var(--ink);
  }
  .brand {
    position: absolute;
    left: 0;
    top: 150px;
    width: 741px;
    text-align: center;
  }
  .brand-square {
    display: block;
    width: 110px;
    height: 110px;
    margin: 0 auto 40px;
    background: var(--mark-grey);
    border-radius: 14px;
  }
  .brand-name {
    margin: 0;
    font-size: 96px;
    font-weight: 400;
    line-height: 1;
    letter-spacing: 4px;
    color: var(--brand-blue);
  }
  .person {
    position: absolute;
    right: 76px;
    top: 535px;
    text-align: right;
  }
  .person-name {
    margin: 0;
    font-size: 66px;
    font-weight: 400;
    line-height: 1;
    letter-spacing: 1px;
  }
  .person-role {
    margin: 10px 0 0;
    font-size: 32px;
    line-height: 1;
    letter-spacing: 1.5px;
  }
  .phone {
    position: absolute;
    right: 76px;
    top: 683px;
    margin: 0;
    font-size: 60px;
    line-height: 1;
    letter-spacing: 1px;
  }
  .contact {
    position: absolute;
    left: 84px;
    top: 972px;
    margin: 0;
    padding: 0;
    list-style: none;
    font-size: 33px;
    line-height: 40px;
    letter-spacing: 1.5px;
  }
  .contact-label {
    font-weight: 700;
    font-family: Arial, Helvetica, sans-serif;
  }
  .footer-band {
    position: absolute;
    left: 0;
    bottom: 0;
    width: 741px;
    height: 126px;
    display: block;
  }
</style>
</head>
<body>
  <div class="card">
    <header class="brand">
      <span class="brand-square" aria-hidden="true"></span>
      <h1 class="brand-name">RVPROMO</h1>
    </header>

    <section class="person">
      <h2 class="person-name">Mark Toveran</h2>
      <p class="person-role">Managing Director</p>
    </section>

    <p class="phone">0481629054</p>

    <ul class="contact">
      <li><span class="contact-label">e:</span> sales@rv-promo.com.au</li>
      <li><span class="contact-label">w:</span> www.rv-promo.com.au</li>
    </ul>

    <svg class="footer-band" viewBox="0 0 741 126" preserveAspectRatio="none" aria-hidden="true">
      <defs>
        <linearGradient id="bandFill" x1="0" y1="0" x2="0" y2="1">
          <stop offset="0" stop-color="var(--band-top)"/>
          <stop offset="1" stop-color="var(--band-bottom)"/>
        </linearGradient>
      </defs>
      <path d="M0 30 Q370 -8 741 30 L741 126 L0 126 Z" fill="url(#bandFill)"/>
    </svg>
  </div>
</body>
</html>
```